Dietary supplement, Clean and simple.

Hi,
I’d like to talk about the project,

About us:
We are a dietary supplement (Vitamins, Minerals, amino acids etc.) company.
The goal is to have about 25 products at the end of this year. However, for this goal to be achieved we need a good label design to make our products represent our company values.
I’ll be here every day supporting your questions, we are fully committed to making the highest/best quality/customer experience possible.

About the design and our values:
- Professional (We are in the industry of professionalism and expertise. I would love to show we are competent at this, Id. Like to have the labels looks like we have done our research.)
- Efficient (White spacing, good use of the space available.)
- Simple (Straight forward, in 5 seconds they have to know what the product they have is/how functions. We’re trying to simplify it for the consumer.
- No distractions (the only visually “distracting” factor can be the vector art.)

The guidelines:
The goal is to have a universal design, with one element that changes (Vector art). I’ll attach a file/multiple files I think can show some visuals on what I’m looking for, and what parts of the design I think are good/bad.

Label size: 69x155mm (Front is 77.5mm)

Design whatever you think fits our image. You’re the design expert, all I care about is that it fits our company standards/image.

Use this color/font.
Font: Sans Serif
Main company color is Mind green #237D62 (Use this color for something in the design.)

What I thought would be cool/might looks ugly, who knows:
1. The front of the label: Should have 1 vector art, preferably in the top right corner. (That looks good in multiple colors. The vector can have multiple areas to color, I would prefer 2 main colors in the vector art. The interchangeable colors are used for multiple kinds of products.)
2. Text/product information on the left. The text that will have to be displayed:
- Product name for instance “Magnesium + B6”
- Description for the product for instance “Magnesium with ginger taste”
- Company name or logo. (Add ® behind it. We are soon to be trademark registered.)
3. We need to show the "daily intake" amount on the front and also the amount in the complete bottle. For instance, “Daily intake 1 capsule, 60 capsules”.
• You don’t have to design the backside of the label. After I chose a design, I’d like to chat and give specific information on what areas need to be assigned where. (Too complex because of the law.)
Updates

Hi, Please make the deadline 31 days total. I want designers to have the time to design. And not be rushed to finish it.

I want to extend the deadline because i feel like a slightly more medical look would be interesting. Hope you can come up with something!!

Target Market(s)

Dietary supplement consumers

Industry/Entity Type

Dietary supplements

Font styles to use
Sans Serif

Colors

Designer to choose colors to be used in the design.

Requirements
Must have
• Trademark icon "®" has to be at the top right after the company logo(text of logo)/name.

```html
<!DOCTYPE html>
<html lang="en">
<head>
<meta charset="utf-8">
<title>Magnesium B+ Label</title>
<link href="https://fonts.googleapis.com/css2?family=Montserrat:wght@400;500;600;700;800&display=swap" rel="stylesheet">
<style>
  :root {
    --plum: #521a40;
    --plum-pill: #7a2466;
    --copper: #b8703f;
    --mint-green: #237d62;
    --white: #ffffff;
  }
  html, body { margin: 0; padding: 0; overflow: hidden; background: var(--white); }
  .label {
    position: relative;
    width: 1200px;
    height: 534px;
    overflow: hidden;
    font-family: "Montserrat", sans-serif;
    background: var(--white);
  }
  .label-backdrop { position: absolute; inset: 0; }
  .brand-box {
    position: absolute;
    left: 734px; top: 34px;
    width: 163px; height: 102px;
    background: var(--white);
    border-radius: 16px 0 0 16px;
    display: flex; align-items: center; justify-content: center;
  }
  .brand-name {
    color: var(--mint-green);
    font-weight: 800;
    font-size: 19px;
    letter-spacing: 0.5px;
    text-align: center;
    line-height: 1.1;
  }
  .title-pill {
    position: absolute;
    left: 383px; top: 191px;
    width: 433px; height: 79px;
    background: var(--white);
    border-radius: 40px;
    text-align: center;
  }
  .product-name {
    margin: 6px 0 0;
    font-size: 53px;
    font-weight: 700;
    color: var(--plum);
    line-height: 1;
    letter-spacing: -0.5px;
  }
  .product-description {
    margin: 3px 0 0;
    font-size: 19.5px;
    font-weight: 500;
    color: var(--copper);
    line-height: 1;
  }
  .variant-badge {
    position: absolute;
    left: 785px; top: 202px;
    width: 55px; height: 55px;
    border-radius: 50%;
    background: radial-gradient(circle at 40% 35%, #3cc0ea, #0f79a8 80%);
    color: var(--white);
    font-weight: 700;
    font-size: 24px;
    display: flex; align-items: center; justify-content: center;
  }
  .fact-pill {
    position: absolute;
    top: 419px;
    width: 139px; height: 38px;
    box-sizing: border-box;
    border: 3px solid var(--plum);
    border-radius: 20px;
    background: linear-gradient(var(--plum-pill), #6a1f58);
    color: var(--white);
    display: flex; flex-direction: column; align-items: center; justify-content: center;
    font-weight: 700;
    font-size: 16px;
    line-height: 1;
  }
  .fact-pill small { font-size: 9px; font-weight: 400; margin-bottom: 1px; }
  .fact-intake { left: 347px; }
  .fact-count { left: 535px; }
  .fact-weight { left: 725px; }
</style>
</head>
<body>
<main class="label">
  <svg class="label-backdrop" width="1200" height="534" viewBox="0 0 1200 534" aria-hidden="true">
    <defs>
      <linearGradient id="copperBand" x1="0" x2="1" y1="0" y2="0">
        <stop offset="0" stop-color="#9a5a2e"/>
        <stop offset="0.45" stop-color="#dca276"/>
        <stop offset="0.72" stop-color="#fcd1a0"/>
        <stop offset="1" stop-color="#c57a45"/>
      </linearGradient>
    </defs>
    <rect width="1200" height="534" fill="var(--white)"/>
    <path d="M0 0 H1200 V46 C900 230 300 260 0 197 Z" fill="var(--plum)"/>
    <path d="M0 197 C300 260 900 230 1200 46 V220 C900 315 300 315 0 220 Z" fill="url(#copperBand)"/>
    <path d="M0 503 Q600 467 1200 503 V534 H0 Z" fill="var(--plum)"/>
    <rect x="45" y="73" width="219" height="425" rx="8" fill="#f3e6f0" fill-opacity="0.55"/>
    <rect x="937" y="73" width="219" height="425" rx="8" fill="#fde0c2" fill-opacity="0.8"/>
  </svg>

  <div class="brand-box">
    <div class="brand-name">NOBLE<br>GROVE®</div>
  </div>

  <div class="title-pill">
    <h1 class="product-name">MAGNESIUM</h1>
    <p class="product-description">Magnesium with lemon taste</p>
  </div>
  <div class="variant-badge">B+</div>

  <div class="fact-pill fact-intake"><small>take daily</small>1 CAPSULE</div>
  <div class="fact-pill fact-count">60 CAPSULES</div>
  <div class="fact-pill fact-weight">180 Grams</div>
</main>
</body>
</html>
```